Web Design Job: Condo Debts Collection Business needs a Web Design

I need a site for a client, who works with condo debts collection, and ensure all revenues provided by condo fees will be always available to the building manager of condo on a specific date, regardless of defaults.
I have the visual identity (logo, slogan and colors) of the company, and some requirements on layout (kind of slider, menu options, phone number on a noble position, etc) - maybe I can do a sketch, but I like the idea of give some freedom to designer.

*** PLEASE, we have no interest in templates. We want something new***
Updates

Reason: We need something new, different and exclusive. We do not want anything that looks like a "template". Thanks.

Target Market(s)

I have two targets for this design:
- Condominium's building manager. This target is looking for a solution to overdue debts on it's condo.
- Residents on condominiums. This target wants to live in a better place, where their neighbors pay their condominium fees on time.

Industry/Entity Type

Business

Number of Pages Required

1 page

Requirements
Must have
• - Slider with title, some short text related, a nice image (I prefer happy and/or peaceful family, people doing business, happy friends, and so on).
• - I have a special attention to menu. I'm looking for one I can have a nice effect, more elegant, charming, kind of innovative.
• - Phone number on the top (or clearly visible).
• - Member log in area or icon on the top (or clearly visible).
• - News/articles area.
• - Modern fonts, with good quality, sans-serif on areas where reading is more intensive (prefer Google web-fonts).
• - Colors specified on attached files.
Nice to have
• - Clear background color, cause it's better to read larger texts (like articles). Dark backgrounds makes reading difficult.
• - A site with effects (like shadows, lines, curves, gradients, lights) is usually pretty.
• - I pay attention on beautiful footers.
Should not have
• - Images with a lot of money (I don't sell richness, I sell tranquility, peace, harmony, safety).
• - Poor menu.

```html
<!DOCTYPE html>
<html lang="en">
<head>
<meta charset="utf-8">
<title>Vértice Cobrança</title>
<link href="https://fonts.googleapis.com/css2?family=Roboto:wght@300;400;500;700&family=Open+Sans:wght@400;600&family=Roboto+Condensed:wght@400&display=swap" rel="stylesheet">
<style>
:root{
  --navy:#1f3572;
  --navy-dark:#172a5e;
  --green:#94a82a;
  --green-dark:#7f9222;
  --nav-blue:#1d3b8c;
  --text:#333;
  --muted:#6b6b6b;
  --line:#e4e4e4;
  --footer:#f1f1f1;
}
*{margin:0;padding:0;box-sizing:border-box}
html,body{width:858px;height:1200px;overflow:hidden;background:#fff}
body{position:relative;font-family:"Open Sans",sans-serif;color:var(--text)}
h1,h2,h3,h4{font-weight:400}
.abs{position:absolute}

.topbar{left:0;top:0;width:858px;height:26px;background:var(--navy)}
.topbar .item{top:7px;font-size:9px;color:#fff;display:flex;align-items:center;gap:6px}
.topbar .divider{left:228px;top:0;width:1px;height:26px;background:rgba(255,255,255,.18)}
.social-top{right:70px;top:7px;display:flex;gap:3px}
.social-top span{width:12px;height:12px;background:#fff;border-radius:2px;display:block}

.header{left:0;top:26px;width:858px;height:84px;background:#fff}
.brand{left:71px;top:60px;display:flex;align-items:center;gap:7px}
.brand .mark{width:20px;height:20px;background:var(--navy)}
.brand .name{font-family:"Roboto",sans-serif;font-weight:500;font-size:13px;color:var(--navy);letter-spacing:.5px}
.nav{position:absolute;left:0;top:30px;width:858px;height:34px}
.nav a{display:block;text-decoration:none;position:absolute;top:0;white-space:nowrap}
.nav .title{font-family:"Roboto",sans-serif;font-size:11px;color:var(--nav-blue);display:block}
.nav .sub{font-size:8px;color:#444;display:block;margin-top:5px}
.nav .sep{position:absolute;top:-2px;width:1px;height:34px;background:#ececec}

.hero{left:0;top:110px;width:858px;height:372px;
  background:linear-gradient(180deg,#3f8fd6 0%,#7fbbe9 35%,#bcdcf2 52%,#6f8f3c 62%,#86a83a 78%,#a0b94c 100%);
  box-shadow:inset 0 8px 10px -6px rgba(0,0,0,.35)}
.hero h1{position:absolute;left:0;width:858px;top:38px;text-align:center;font-family:"Roboto",sans-serif;font-weight:700;font-size:36px;color:#fff;text-shadow:0 2px 4px rgba(0,0,0,.3)}
.hero p{position:absolute;left:190px;width:478px;top:88px;text-align:center;font-family:"Roboto",sans-serif;font-size:9px;line-height:15px;color:#fff}
.hero .arrow{position:absolute;top:169px;width:25px;height:25px;border-radius:50%;background:rgba(40,70,110,.7)}

.welcome-title{left:70px;top:516px;font-family:"Roboto",sans-serif;font-weight:300;font-size:20px;color:#333}
.video{left:71px;top:556px;width:205px;height:185px;background:linear-gradient(180deg,#6f95c8 0%,#a9c3e0 45%,#546d86 70%,#3c6b2c 100%);border:1px solid #ddd}
.intro-head{left:297px;top:550px;width:260px;font-family:"Roboto",sans-serif;font-weight:300;font-size:14px;line-height:20px;color:#333}
.intro-text{left:297px;width:270px;font-size:8px;line-height:14.5px;color:#666}
.read-more{left:296px;top:711px;width:101px;height:30px;border:1px solid #e2e2e2;border-radius:2px;background:linear-gradient(#fff,#f2f2f2);font-family:"Roboto",sans-serif;font-size:10px;color:var(--navy);display:flex;align-items:center;justify-content:center;box-shadow:0 1px 2px rgba(0,0,0,.06)}

.restricted{left:607px;top:519px;width:181px;height:222px;background:var(--navy);overflow:hidden}
.restricted .head{position:absolute;left:0;top:0;width:181px;height:44px}
.restricted .head span{position:absolute;left:0;top:12px;width:181px;text-align:center;font-family:"Roboto",sans-serif;font-size:13px;color:#fff}
.field{position:absolute;left:15px;width:152px;height:27px;background:#fff;font-family:"Roboto",sans-serif;font-size:9px;color:#333;display:flex;align-items:center;justify-content:center}
.subscribe{position:absolute;left:15px;top:135px;width:152px;height:27px;background:var(--green);border-radius:2px;font-family:"Roboto",sans-serif;font-size:9px;color:#fff;display:flex;align-items:center;justify-content:center}
.restricted .note{position:absolute;left:0;width:181px;top:175px;text-align:center;font-family:"Roboto Condensed",sans-serif;font-size:10px;line-height:15px;color:#fff}
.restricted .note u{color:#fff}

.rule{left:70px;top:779px;width:718px;height:1px;background:var(--line)}
.news-title{left:70px;top:801px;font-family:"Roboto",sans-serif;font-weight:300;font-size:19px;color:#333}
.card{top:839px;width:170px}
.card .photo{width:170px;height:117px}
.card h3{margin-top:13px;font-family:"Roboto",sans-serif;font-weight:300;font-size:12px;color:#333}
.card .date{margin-top:8px;font-family:"Roboto",sans-serif;font-size:9px;color:var(--navy);display:flex;align-items:center;gap:4px}
.card p{margin-top:7px;font-size:8px;line-height:16px;color:#555}
.card .dots{margin-top:6px;border-top:1px dotted #ccc}

.footer{left:0;top:1110px;width:858px;height:90px;background:var(--footer);border-top:1px solid #e6e6e6}
.f-brand{left:70px;top:1145px;display:flex;align-items:center;gap:5px}
.f-brand .mark{width:24px;height:24px;border-radius:50%;background:#2e7d32}
.f-brand .name{font-family:"Roboto",sans-serif;font-weight:400;font-size:9px;color:#2e7d32;letter-spacing:.2px}
.copy{left:182px;top:1139px;font-size:8.5px;color:#333}
.f-links{left:182px;top:1163px;font-size:8.5px;color:#333}
.f-social{left:484px;top:1146px;display:flex;gap:4px}
.f-social span{width:18px;height:18px;border-radius:50%;display:block}
.nl-title{left:590px;top:1133px;font-family:"Roboto",sans-serif;font-weight:400;font-size:10.5px;color:#333;letter-spacing:.3px}
.nl-input{left:590px;top:1154px;width:137px;height:23px;background:#fff;border:1px solid #ddd;font-size:8px;color:#888;padding-left:10px;display:flex;align-items:center}
.nl-btn{left:731px;top:1154px;width:56px;height:23px;background:var(--navy);border-radius:2px;color:#fff;font-family:"Roboto",sans-serif;font-size:9.5px;display:flex;align-items:center;justify-content:center}
</style>
</head>
<body>

<div class="abs topbar">
  <div class="abs item" style="left:70px">
    <svg width="8" height="8" viewBox="0 0 10 10"><path d="M2 0.5l2 2-1 1.3c.6 1.3 1.6 2.3 2.9 2.9l1.3-1 2 2-1.2 1.8C4.4 9.3.7 5.6.3 1.7z" fill="#fff"/></svg>
    (31) 3000 1234 / (31) 7000 5678
  </div>
  <div class="abs divider"></div>
  <div class="abs item" style="left:248px">
    <svg width="7" height="8" viewBox="0 0 8 10"><rect x="0.5" y="4" width="7" height="5.5" fill="#fff"/><path d="M2 4V2.6a2 2 0 014 0V4" fill="none" stroke="#fff" stroke-width="1.2"/></svg>
    Member log in
  </div>
  <div class="abs social-top"><span></span><span></span><span></span></div>
</div>

<div class="abs header">
  <nav class="nav">
    <a style="left:387px"><span class="title">HOME</span><span class="sub">Start page</span></a>
    <span class="sep" style="left:440px"></span>
    <a style="left:466px"><span class="title">ABOUT US</span><span class="sub">Who we are</span></a>
    <span class="sep" style="left:535px"></span>
    <a style="left:558px"><span class="title">SERVICES</span><span class="sub">What we offer</span></a>
    <span class="sep" style="left:629px"></span>
    <a style="left:652px"><span class="title">SOLUTIONS</span><span class="sub">Our works</span></a>
    <span class="sep" style="left:718px"></span>
    <a style="left:742px"><span class="title">CONTACT</span><span class="sub">Get in touch</span></a>
  </nav>
</div>
<div class="abs brand"><span class="mark"></span><span class="name">VÉRTICE COBRANÇA</span></div>

<section class="abs hero" role="img" aria-label="Happy family running hand in hand across a sunny green meadow under a blue sky">
  <h1>Vértice Cobrança</h1>
  <p>Duis aute irure dolor in reprehenderit in voluptate velit esse cillum dolore eu fugiat nulla pariatur. Excepteur sint occaecat cupidatat non proident, sunt in culpa qui officia deserunt mollit anim id est laborum</p>
  <span class="arrow" style="left:29px"><svg width="25" height="25" viewBox="0 0 25 25"><path d="M14.5 7.5l-5 5 5 5" fill="none" stroke="#fff" stroke-width="1.6"/></svg></span>
  <span class="arrow" style="left:802px"><svg width="25" height="25" viewBox="0 0 25 25"><path d="M10.5 7.5l5 5-5 5" fill="none" stroke="#fff" stroke-width="1.6"/></svg></span>
</section>

<h2 class="abs welcome-title">Welcome To&nbsp; Vértice Cobrança</h2>
<div class="abs video" role="img" aria-label="Video thumbnail of city skyscrapers above a green park">
  <svg width="205" height="185" viewBox="0 0 205 185"><circle cx="102" cy="92" r="23" fill="rgba(255,255,255,.35)" stroke="#2b2b2b" stroke-width="2.5"/><path d="M95 80v24l19-12z" fill="#2b2b2b"/></svg>
</div>
<h3 class="abs intro-head">Duis aute irure dolor in reprehenderit in voluptate velit esse</h3>
<p class="abs intro-text" style="top:600px">Lorem ipsum dolor sit amet, consectetur adipiscing elit, sed do eiusmod tempor incididunt ut labore et dolore magna aliqua. Ut enim ad minim veniam, quis nostrud exercitation ullamco laboris nisi ut aliquip</p>
<p class="abs intro-text" style="top:650px">Lorem ipsum dolor sit amet, consectetur adipiscing elit, sed do eiusmod tempor incididunt ut labore et dolore magna aliqua. Ut enim ad minim veniam, quis nostrud exercitation ullamco laboris nisi ut aliquip</p>
<div class="abs read-more">READ MORE &gt;&gt;</div>

<aside class="abs restricted">
  <svg class="head" width="181" height="44" viewBox="0 0 181 44"><path d="M0 0H181V36Q90 50 0 33Z" fill="var(--green)"/><path d="M0 33Q90 50 181 36V40Q90 54 0 37Z" fill="var(--green-dark)"/></svg>
  <div class="head"><span>RESTRICTED AREA</span></div>
  <div class="field" style="top:63px">Your Name</div>
  <div class="field" style="top:98px">E - Mail Address</div>
  <div class="subscribe">SUBSCRIBE</div>
  <p class="note">If you do not know your<br>ID, <u>click here</u></p>
</aside>

<div class="abs rule"></div>
<h2 class="abs news-title">Featured News</h2>

<article class="abs card" style="left:71px">
  <div class="photo" role="img" aria-label="Group of cheerful friends outdoors under a cloudy sky" style="background:linear-gradient(180deg,#b9cfe2,#d8d2c4 60%,#a8937a)"></div>
  <h3>Nemo Enim Ipsam Voluptatem</h3>
  <div class="date"><svg width="8" height="8" viewBox="0 0 10 10"><circle cx="5" cy="5" r="4" fill="none" stroke="var(--navy)" stroke-width="1.6"/><path d="M5 2.5V5h2" fill="none" stroke="var(--navy)" stroke-width="1.2"/></svg>19.00 pm - 10 / 2015</div>
  <p>Vivamus elementum semper nisi.&nbsp; Lorem ipsum met, sectetuer adipiscing elit. Aenean commodoVivamus</p>
  <div class="dots"></div>
</article>
<article class="abs card" style="left:253px">
  <div class="photo" role="img" aria-label="Smiling family lying on grass beside a drawn blue house" style="background:linear-gradient(180deg,#2f7fd0,#8cc0ea 55%,#5fa83a 80%,#3e8a24)"></div>
  <h3>Nemo Enim Ipsam Voluptatem</h3>
  <div class="date"><svg width="8" height="8" viewBox="0 0 10 10"><circle cx="5" cy="5" r="4" fill="none" stroke="var(--navy)" stroke-width="1.6"/><path d="M5 2.5V5h2" fill="none" stroke="var(--navy)" stroke-width="1.2"/></svg>19.00 pm - 10 / 2015</div>
  <p>Vivamus elementum semper nisi.&nbsp; Lorem ipsum met, sectetuer adipiscing elit. Aenean commodoVivamus</p>
  <div class="dots"></div>
</article>
<article class="abs card" style="left:436px">
  <div class="photo" role="img" aria-label="Business people meeting in a bright modern office" style="background:linear-gradient(180deg,#e6e9ec,#cfd5da 55%,#8a8f95)"></div>
  <h3>Nemo Enim Ipsam Voluptatem</h3>
  <div class="date"><svg width="8" height="8" viewBox="0 0 10 10"><circle cx="5" cy="5" r="4" fill="none" stroke="var(--navy)" stroke-width="1.6"/><path d="M5 2.5V5h2" fill="none" stroke="var(--navy)" stroke-width="1.2"/></svg>19.00 pm - 10 / 2015</div>
  <p>Vivamus elementum semper nisi.&nbsp; Lorem ipsum met, sectetuer adipiscing elit. Aenean commodoVivamus</p>
  <div class="dots"></div>
</article>
<article class="abs card" style="left:618px">
  <div class="photo" role="img" aria-label="City skyline at dusk with lit towers reflected on water" style="background:linear-gradient(180deg,#6c5aa8,#b57aa8 45%,#4a2f5a 70%,#2a2340)"></div>
  <h3>Nemo Enim Ipsam Voluptatem</h3>
  <div class="date"><svg width="8" height="8" viewBox="0 0 10 10"><circle cx="5" cy="5" r="4" fill="none" stroke="var(--navy)" stroke-width="1.6"/><path d="M5 2.5V5h2" fill="none" stroke="var(--navy)" stroke-width="1.2"/></svg>19.00 pm - 10 / 2015</div>
  <p>Vivamus elementum semper nisi.&nbsp; Lorem ipsum met, sectetuer adipiscing elit. Aenean commodoVivamus</p>
  <div class="dots"></div>
</article>

<footer class="abs footer"></footer>
<div class="abs f-brand"><span class="mark"></span><span class="name">NORTE ADVOCACIA</span></div>
<p class="abs copy">©2015 Vértice Cobrança. , All Rights Reserved.</p>
<p class="abs f-links">Home&nbsp; |&nbsp; About Us&nbsp; |&nbsp; Web Design&nbsp; |&nbsp; Sign Up&nbsp; |&nbsp; Contact Us</p>
<div class="abs f-social"><span style="background:#3b5a9a"></span><span style="background:#2a9fd8"></span><span style="background:#d8302a"></span></div>
<h4 class="abs nl-title">NEWSLETTER SIGN UP</h4>
<div class="abs nl-input">Enter Your Email</div>
<div class="abs nl-btn">Subscribe</div>

</body>
</html>
```